Flyer for photo scanning business

Hello,
I need a flyer created for my business that would be suitable for print, to drop in letterboxes in my local community.

I would like the flyer to convey very simply the services I offer which is scanning negatives, slides and VHS tapes to digital files.
Hopefully it can make it look like an easy process, as people are often daunted by the task of sorting through old photos so they don't always get around to having them scanned.

I have a pinned facebook post that can be used by the designer to reference my services. Pricing does not need to be included on the flyer.
http://facebook.com/brightvaleimaging

Target Market(s)

Parents & Grandparents

Requirements
Must have
• Must make my services look simple! Refer to pinned facebook post for detailed outline of my services.

I would like to flyer to point towards my contact details -
www.brightvale.com
Margot 0478 219 836

Colours in line with my logo/brand (uploaded to brief).
Nice to have
• Stock images of 35mm film negatives, 8mm film, VHS tapes, or Lumavert slides would be worth including. I have also uploaded a mockup of the USB sticks that I provide with digitised images.
Should not have
• no prices needed,

```html
<!DOCTYPE html>
<html lang="en">
<head>
<meta charset="utf-8">
<title>Brightvale Imaging – Flyer</title>
<link href="https://fonts.googleapis.com/css2?family=Montserrat:wght@300;400;500;700;800&display=swap" rel="stylesheet">
<style>
  :root{
    --navy:#2a65a0;
    --sky:#6ab2dc;
    --sky-pale:#d6e7f5;
    --ink:#2b2b2b;
    --body:#333;
    --white:#fff;
  }
  *{margin:0;padding:0;box-sizing:border-box}
  html,body{width:1200px;height:1200px;overflow:hidden}
  body{background:var(--navy);position:relative;font-family:"Montserrat",sans-serif}
  .flyer{position:absolute;left:214px;top:55px;width:772px;height:1090px;background:var(--white);overflow:hidden}
  .abs{position:absolute}
  .top-band{left:0;top:0;width:772px;height:31px;background:var(--sky)}
  .header-strip{left:0;top:31px;width:772px;height:117px}
  .brand-box{left:229px;top:43px;width:313px;height:89px;background:var(--navy);color:var(--white);text-align:right;padding:20px 16px 0 0}
  .brand-mark{position:absolute;left:20px;top:26px;width:34px;height:34px;border-radius:50%;background:var(--sky)}
  .brand-name{font-size:29px;font-weight:400;letter-spacing:3px;line-height:30px}
  .brand-sub{font-size:16px;font-weight:400;letter-spacing:4px;line-height:20px}
  .photo{background:linear-gradient(135deg,var(--c1),var(--c2))}
  .photo-film{left:0;top:161px;width:135px;height:375px;--c1:#2c2f3d;--c2:#6b5a3a}
  .photo-usb{left:152px;top:161px;width:347px;height:115px;--c1:#a9c3de;--c2:#5d89b8}
  .photo-vhs{left:152px;top:292px;width:347px;height:244px;--c1:#c9c9c9;--c2:#2a2a2a}
  .photo-camera{left:514px;top:161px;width:258px;height:375px;--c1:#3fb2d8;--c2:#5a4a3e}
  .photo-negatives{left:393px;top:621px;width:107px;height:174px;--c1:#f2f2f2;--c2:#6a5a4a}
  .photo-reels{left:393px;top:814px;width:107px;height:174px;--c1:#3a3a3a;--c2:#b89a7a}
  .photo-border{border-right:2px solid var(--sky)}
  .headline-box{left:32px;top:465px;width:346px;height:158px;background:var(--sky)}
  .headline-accent{left:349px;top:492px;width:43px;height:103px;background:var(--navy)}
  .headline{left:40px;top:470px;width:320px;font-size:37px;font-weight:700;line-height:46.5px;color:var(--ink)}
  .section-title{font-size:19.5px;font-weight:700;color:var(--navy);line-height:22px}
  .rule{height:2px;background:var(--ink)}
  .body-copy{font-size:13.6px;font-weight:400;line-height:17.1px;color:var(--body);text-align:justify;letter-spacing:.15px}
  .about-title{left:32px;top:650px}
  .about-rule{left:32px;top:674px;width:72px}
  .about-1{left:32px;top:684px;width:346px}
  .about-2{left:32px;top:829px;width:346px}
  .services-title{left:514px;top:586px}
  .services-rule{left:514px;top:612px;width:47px}
  .service-title{font-size:18.5px;font-weight:700;color:var(--sky);line-height:22px}
  .neg-title{left:514px;top:630px;width:230px}
  .neg-copy{left:514px;top:688px;width:226px}
  .vhs-title{left:514px;top:811px}
  .vhs-copy{left:514px;top:847px;width:226px}
  .vhs-copy p+p{margin-top:17px}
  .footer-band{left:0;top:1027px;width:772px;height:44px;background:var(--navy)}
  .footer-base{left:0;top:1073px;width:772px;height:17px;background:var(--sky)}
  .help-icon{left:26px;top:975px}
  .contact-label{left:126px;top:1032px;font-size:27px;font-weight:700;color:var(--white)}
  .phone{left:350px;top:1038px;font-size:19px;font-weight:700;color:var(--white);display:flex;align-items:center;gap:5px}
  .web{left:572px;top:1040px;font-size:12.5px;color:var(--white);display:flex;align-items:center;gap:6px}
</style>
</head>
<body>
<div class="flyer">
  <div class="abs top-band"></div>
  <svg class="abs header-strip" width="772" height="117" viewBox="0 0 772 117">
    <defs>
      <linearGradient id="stripGrad" x1="0" x2="1">
        <stop offset="0" stop-color="#8fc2e6"/>
        <stop offset=".3" stop-color="#dbe9f6"/>
        <stop offset=".7" stop-color="#dbe9f6"/>
        <stop offset="1" stop-color="#8fc2e6"/>
      </linearGradient>
    </defs>
    <rect x="0" y="0" width="772" height="117" fill="var(--navy)"/>
    <rect x="0" y="12" width="772" height="89" fill="url(#stripGrad)"/>
    <line x1="0" y1="6" x2="772" y2="6" stroke="#fff" stroke-width="1" stroke-dasharray="14 8"/>
    <line x1="0" y1="109" x2="772" y2="109" stroke="#fff" stroke-width="1" stroke-dasharray="14 8"/>
  </svg>
  <div class="abs" style="left:0;top:150px;width:772px;height:2px;background:var(--sky)"></div>
  <div class="abs brand-box">
    <span class="brand-mark"></span>
    <div class="brand-name">BRIGHTVALE</div>
    <div class="brand-sub">IMAGING</div>
  </div>

  <div class="abs photo photo-film" role="img" aria-label="Close-up of film reels and coloured slide mounts"></div>
  <div class="abs photo photo-usb" role="img" aria-label="Branded USB drives on a blue surface"></div>
  <div class="abs photo photo-vhs" role="img" aria-label="Stack of VHS tapes"></div>
  <div class="abs photo photo-camera" role="img" aria-label="Vintage film camera lens on a blue textured surface"></div>
  <div class="abs" style="left:0;top:544px;width:772px;height:1px;background:var(--sky-pale)"></div>

  <div class="abs headline-box"></div>
  <div class="abs headline-accent"></div>
  <h1 class="abs headline">Ducil et abor sequi dellacc uptatur ma de</h1>

  <h2 class="abs section-title about-title">ABOUT US</h2>
  <div class="abs rule about-rule"></div>
  <p class="abs body-copy about-1">Sinulliquati disto corrovi tiunto blaut acil eum repedit asperibus abo. Nem il il iducia sitae nonsequi tectatatquam qui apiducipit omnit doluptatur, to eos sit, ad quam solorrorest, quostia nimus pore officim aximus, offici re, sita comnihilit landae paribusandis suntur simus utemper ferspel iquisciis</p>
  <p class="abs body-copy about-2">Sinulliquati disto corrovi tiunto blaut acil eum repedit asperibus abo. Nem il il iducia sitae nonsequi tectatatquam qui apiducipit omnit doluptatur, to eos sit, ad quam solorrorest, quostia nimus pore officim aximus, offici re, sita comnihilit landae paribusandis suntur simus utemper ferspel iquisciis</p>

  <h2 class="abs section-title services-title">OUR SERVICES</h2>
  <div class="abs rule services-rule"></div>
  <div class="abs photo photo-negatives photo-border" role="img" aria-label="Film negative strips and slide holders"></div>
  <h3 class="abs service-title neg-title">Photo Negative Scanning</h3>
  <p class="abs body-copy neg-copy">Digitising photo slides and negatives. Your photos will be personally picked up and delivered back to your home with high resolution JPEG files on a USB drive.</p>
  <div class="abs photo photo-reels photo-border" role="img" aria-label="Laptop beside film reels and tapes on a wooden desk"></div>
  <h3 class="abs service-title vhs-title">VHS Digitising</h3>
  <div class="abs body-copy vhs-copy">
    <p>Conversion of VHS tapes to computer friendly video files using high quality broadcast equipment.</p>
    <p>Your tapes will be personally picked up and returned to your home with a USB drive.</p>
  </div>

  <div class="abs footer-band"></div>
  <div class="abs footer-base"></div>
  <svg class="abs help-icon" width="90" height="82" viewBox="0 0 90 82">
    <path d="M52 22 a30 28 0 1 1 -10 54 l-4 4 2 -10 a30 28 0 0 1 12 -48z" fill="#fff" stroke="var(--navy)" stroke-width="4"/>
    <path d="M33 4 a30 29 0 1 1 -14 55 l-13 6 5 -13 a30 29 0 0 1 22 -48z" fill="#fff" stroke="var(--navy)" stroke-width="4"/>
    <text x="33" y="45" text-anchor="middle" font-family="Montserrat,sans-serif" font-weight="800" font-size="32" fill="var(--navy)">?</text>
  </svg>
  <div class="abs contact-label">Contact Us</div>
  <div class="abs phone">
    <svg width="20" height="20" viewBox="0 0 24 24"><path d="M6.6 10.8c1.4 2.8 3.8 5.1 6.6 6.6l2.2-2.2c.3-.3.7-.4 1-.2 1.1.4 2.3.6 3.6.6.6 0 1 .4 1 1V20c0 .6-.4 1-1 1C10.6 21 3 13.4 3 4c0-.6.4-1 1-1h3.5c.6 0 1 .4 1 1 0 1.3.2 2.5.6 3.6.1.3 0 .7-.2 1z" fill="#fff"/></svg>
    0478 219 836
  </div>
  <div class="abs web">
    <svg width="19" height="19" viewBox="0 0 20 20"><circle cx="10" cy="10" r="8.5" fill="none" stroke="#fff" stroke-width="1.3"/><ellipse cx="10" cy="10" rx="3.5" ry="8.5" fill="none" stroke="#fff" stroke-width="1.1"/><line x1="1.5" y1="10" x2="18.5" y2="10" stroke="#fff" stroke-width="1.1"/></svg>
    www.brightvale.com
  </div>
</div>
</body>
</html>
```